Can design for new all natural low calorie spiked lemonade

We need a clean but catchy can design for a new spiked lemonade that will be all natural, gluten free and low in calories. Open to any creative ideas ranging from designs such as using a lemonade stand to simple designs such as the example pictures that are uploaded. Looking for a can that just pops out right away on the shelf but also believe less is more as far as simplicity. The beverage is called Brightlow Spiked Lemonade, that features 3 flavors. Traditional Lemonade, Peach Lemonade and lastly Strawberry Lemonade.

Target Market(s)

21-55 years of age. 75% female, 25% male.

Colors

Designer to choose colors to be used in the design.

Requirements
Must have
• The brand name is Brightlow and it is a spiked lemonade so that should be catchy so the consumer knows what it is on first glance. Must say gluten free, all natural, and 150 calories on the front of the can. Would like some type of image on the front middle of the can. There are 3 flavors so the can should blend well with each fruit but not be different cans

```html
<!DOCTYPE html>
<html lang="en">
<head>
<meta charset="utf-8">
<title>Brightlow Spiked Lemonade – Can Label</title>
<link rel="stylesheet" href="https://fonts.googleapis.com/css2?family=Montserrat:wght@400;500&display=swap">
<style>
  :root {
    --backdrop: #efeeea;
    --label-white: #fbfbfa;
    --lemon-band: #cdb63c;
    --lemon-band-light: #ddc95a;
    --gold-text: #b0941f;
    --white-text: #ffffff;
    --photo-tone-a: #ecd54a;
    --photo-tone-b: #f6f1d8;
  }
  * { box-sizing: border-box; margin: 0; padding: 0; }
  html, body {
    width: 1200px; height: 789px; overflow: hidden;
    background: var(--backdrop);
    font-family: "Montserrat", sans-serif;
  }
  .canvas {
    position: relative; width: 1200px; height: 789px;
  }
  .can-label {
    position: absolute; left: 380px; top: 34px;
    width: 440px; height: 720px;
    background: var(--label-white);
    box-shadow: 0 2px 10px rgba(0,0,0,0.08);
    overflow: hidden;
  }
  .top-band {
    position: absolute; left: 0; top: 0; width: 100%; height: 104px;
    background: linear-gradient(180deg, var(--lemon-band-light), var(--lemon-band));
    display: flex; align-items: flex-end; justify-content: center;
    padding-bottom: 14px;
  }
  .tagline {
    color: var(--white-text); font-size: 17px; font-weight: 400; letter-spacing: 0.3px;
  }
  .flavour-ribbon {
    position: absolute; left: 50%; top: 104px; transform: translateX(-50%);
    width: 136px; height: 78px;
    background: var(--lemon-band);
    color: var(--white-text); font-size: 16px; line-height: 17px; text-align: center;
    padding-top: 18px;
  }
  .brand-name {
    position: absolute; left: 0; top: 268px; width: 100%;
    text-align: center; color: var(--gold-text);
    font-size: 52px; font-weight: 400; letter-spacing: 1px;
  }
  .fruit-image {
    position: absolute; left: 150px; top: 420px; width: 150px; height: 120px;
    background: radial-gradient(ellipse at 60% 45%, var(--photo-tone-a) 0%, var(--photo-tone-b) 75%, var(--label-white) 100%);
  }
  .claims {
    position: absolute; left: 0; top: 578px; width: 100%;
    text-align: center; color: var(--gold-text);
    font-size: 16px; line-height: 21px; letter-spacing: 0.3px; text-transform: uppercase;
  }
  .volume {
    position: absolute; left: 0; top: 650px; width: 100%;
    text-align: center; color: var(--gold-text); font-size: 15px;
  }
</style>
</head>
<body>
<main class="canvas">
  <section class="can-label">
    <div class="top-band"><p class="tagline">new spiked lemonade</p></div>
    <div class="flavour-ribbon">Traditional<br>Lemonade</div>
    <h1 class="brand-name">Brightlow</h1>
    <div class="fruit-image" role="img" aria-label="Photo of a whole lemon with a sprig of mint leaves"></div>
    <p class="claims">Gluten free &bull; All natural<br>150 calories</p>
    <p class="volume">250ml</p>
  </section>
</main>
</body>
</html>
```